Construction Company Website Design

I need a Website Design for a Construction Company. I have attached logo and business card design files (a.i) to match styles and text for the website. I will need design for 3 pages:
1. A Home page
2. A secondary page (will be different information pages)
3. A contact page with submision form
Website to look professional and match the 'theme' across all pages, using main colours / reverse colours as per design files. Must be clear it is a construction related website without being over the top. Happy for the construction related details (whether that be images/outlines/backgrounds etc to be fairly subtle and not overbearing on the contect of the pages. It will be the content that will be most important, not the images within.

Content has not yet been fully completed but attached is a site map. Each page will need a space for the insertion of the relevant heading and associated content for that particular page. Example can be used as per attached map. If it is preferable to have content completed for this to be a more succesful project please advise and I will complete and submit.

Target Market(s)

Clients for potential construction projects. These could be a range of people. All would be very professional, well educated and put a substantial expection on the quality of website provided.

Industry/Entity Type

Construction

Number of Pages Required

3 page

Font styles to use
Serif
Sans Serif
Other font styles liked:
• fonts preferable as per design files provided unless designer beleives a different font would suit better

Requirements
Must have
• Colour scheme to match logo and business card files provided. Fonts that match as per provided files. Pages must be consistent with the theme carrying across all pages. All pages must have contact details at the bottom of the page.
• Contents of page 1 - 'Home page': multiple tab options / logo link
• Contents of page 2 - 'Secondary page': Top and side navigation / area for information and/or images.
• Contents of page - 'Contact us page': Top and side navigation / Submission form / area for logos such as linkdin, facebook etc.
Nice to have
• Would be good to have a or some generic construction related images - outlines / shadows / effects etc. These might be background images or outlines related to the relevant industry and are consistent across the pages. Could be outlines of buildings, images of men with hardhats etc etc. Good to see colour scheme as per design files used
Should not have
• No pictures of houses. Generally no photos. If any imagery of people must not show faces/details.

```html
<!DOCTYPE html>
<html lang="en">
<head>
<meta charset="utf-8">
<title>KRD Constructions</title>
<link href="https://fonts.googleapis.com/css2?family=Michroma&family=Lato:wght@400;700;900&display=swap" rel="stylesheet">
<style>
:root{
  --blue:#1ba6e6;
  --blue-dark:#0f8bc7;
  --ink:#2d3138;
  --text:#5b616b;
  --muted:#9aa1aa;
  --pale:#eef6fc;
  --line:#dfe6ee;
  --white:#ffffff;
}
*{box-sizing:border-box;margin:0;padding:0}
html,body{width:1200px;height:3750px;overflow:hidden}
body{font-family:"Lato",sans-serif;color:var(--text);background:var(--white);position:relative}
.abs{position:absolute}
.display{font-family:"Michroma",sans-serif;letter-spacing:1px}

/* Hero */
.hero{position:absolute;left:0;top:0;width:1200px;height:600px;
  background:linear-gradient(160deg,#3b4654 0%,#1f2a36 45%,#2f3c4a 70%,#1a222c 100%)}
.brand{left:110px;top:32px;color:var(--white);font-family:"Lato",sans-serif;font-weight:700;font-size:20px;letter-spacing:1px;display:flex;align-items:center;gap:10px}
.brand .mark{width:12px;height:12px;background:var(--white)}
.nav{right:110px;top:38px;display:flex;font-weight:700;font-size:12px;letter-spacing:1px;color:var(--white)}
.nav a{color:inherit;text-decoration:none;padding:0 12px;border-left:1px solid rgba(255,255,255,.4)}
.nav a:first-child{border-left:0}
.hero-title{left:360px;top:240px;width:480px;height:90px;background:rgba(20,28,38,.55);text-align:center;padding-top:12px}
.hero-title .l1{color:var(--blue);font-size:31px;line-height:38px}
.hero-title .l2{color:var(--white);font-size:24px;line-height:30px}
.btn{display:inline-block;background:var(--blue);color:var(--white);font-weight:700;font-size:11px;letter-spacing:1px;padding:10px 16px;text-transform:uppercase}
.hero .btn{position:absolute;left:533px;top:345px}
.hero-bar{left:110px;top:555px;display:flex;gap:30px;color:var(--white);font-size:12px;align-items:center}
.hero-bar span{display:flex;align-items:center;gap:10px}
.icon-dot{width:22px;height:22px;border-radius:50%;background:rgba(255,255,255,.15);display:flex;align-items:center;justify-content:center}
.socials{display:flex;gap:10px}
.socials i{display:block;width:24px;height:24px;border-radius:50%;border:1px solid rgba(255,255,255,.7)}
.hero .socials{position:absolute;right:110px;top:553px}

/* Welcome */
.welcome-back{left:210px;top:660px;width:265px;height:330px;background:var(--blue)}
.welcome-photo{left:258px;top:700px;width:267px;height:330px;background:linear-gradient(180deg,#e9a27e 0%,#b87a8a 45%,#5a6a88 100%);box-shadow:0 8px 24px rgba(0,0,0,.2)}
.welcome-text{left:580px;top:695px;width:410px}
.welcome-text .kicker{font-size:20px;color:var(--ink)}
.welcome-text .company{font-family:"Michroma",sans-serif;font-size:24px;color:var(--ink);margin-top:14px}
.welcome-text p{font-size:12.5px;line-height:24px;margin-top:18px}
.welcome-text .btn{margin-top:30px}

/* Section titles */
.sec-title{left:0;width:1200px;text-align:center;font-family:"Michroma",sans-serif;font-size:24px;letter-spacing:1px;color:var(--ink)}

/* Services */
.services{left:0;top:1100px;width:1200px;height:460px;background:var(--pale)}
.card{background:var(--white);box-shadow:0 4px 14px rgba(0,0,0,.08)}
.service{width:175px;height:262px}
.service .ph{height:205px;background:linear-gradient(180deg,#d4d8dd,#a4abb4)}
.service.active .ph{background:linear-gradient(180deg,#6f7d8c,#3c4652)}
.service.active{background:#2e343c}
.service .label{text-align:center;font-family:"Michroma",sans-serif;font-size:10px;letter-spacing:1px;line-height:15px;padding-top:12px;color:var(--ink)}
.service.active .label{color:var(--white)}

/* Projects */
.filters{left:0;top:1672px;width:1200px;display:flex;justify-content:center;gap:22px;font-size:11px;font-weight:700;letter-spacing:1px;color:var(--text)}
.filters .on{color:var(--blue);border-bottom:2px solid var(--blue);padding-bottom:3px}
.proj{background:linear-gradient(160deg,#cfe3f3,#5e8fbd)}

/* Testimonials */
.testi{left:0;top:2170px;width:1200px;height:385px;background:var(--pale)}
.avatar{left:260px;top:2318px;width:130px;height:130px;border-radius:50%;border:5px solid var(--white);background:linear-gradient(180deg,#c6d6e4,#7a8da0);box-shadow:0 4px 14px rgba(0,0,0,.12)}
.avatar-badge{left:245px;top:2395px;width:62px;height:62px;border-radius:50%;background:var(--white);border:3px solid var(--blue)}
.quote-mark{left:412px;top:2305px;font-family:Georgia,serif;font-size:70px;color:#cdd6df;line-height:1}
.quote{left:458px;top:2318px;width:535px;font-style:italic;font-size:13px;line-height:23px;color:var(--muted)}
.who{left:458px;top:2445px;font-size:13px;color:var(--ink)}
.who b{font-weight:700;letter-spacing:1px;margin-right:18px}
.stars{left:458px;top:2470px;color:var(--blue);font-size:13px;letter-spacing:1px}

/* News */
.news{width:233px;height:305px}
.news .ph{height:165px;background:linear-gradient(180deg,#9fc7e4,#4e6f8d)}
.news .badge-ic{position:absolute;left:100px;top:146px;width:34px;height:34px;border-radius:50%;background:#3a4048;border:3px solid var(--white)}
.news .date{position:absolute;left:0;top:200px;width:28px;height:42px;background:var(--blue);color:var(--white);text-align:center;font-weight:900;font-size:15px;line-height:24px}
.news .date small{display:block;font-size:7px;line-height:8px;font-weight:700}
.news h4{position:absolute;left:40px;top:198px;width:180px;font-size:10px;line-height:14px;color:var(--ink);font-weight:900}
.news p{position:absolute;left:40px;top:232px;width:180px;font-size:9px;line-height:13px;color:var(--muted);font-style:italic}
.news p span{color:var(--blue)}

/* Map & contact */
.map{left:0;top:3070px;width:1200px;height:420px;background:linear-gradient(135deg,#eef0f2,#e3e7ea 50%,#edf1ee)}
.map-pin{left:588px;top:3192px}
.form{left:210px;top:3262px;width:522px;height:333px;background:var(--white);box-shadow:0 6px 20px rgba(0,0,0,.1);padding:30px 35px}
.form h3,.contact h3{font-family:"Michroma",sans-serif;font-weight:400;font-size:16px;letter-spacing:1px}
.form h3{color:var(--blue)}
.fields{display:grid;grid-template-columns:1fr 1fr;gap:12px;margin-top:20px}
.field{border:1px solid var(--line);height:30px;font-size:10px;color:var(--muted);padding:8px 10px}
.field.wide{grid-column:1/3}
.field.tall{height:78px}
.form .btn{margin-top:16px}
.contact{left:732px;top:3262px;width:258px;height:333px;background:var(--blue);color:var(--white);padding:30px 30px}
.c-row{display:flex;gap:12px;margin-top:20px;font-size:11px;line-height:17px}
.c-row b{font-weight:900;letter-spacing:1px}
.contact .socials{margin-top:24px;justify-content:center}
.contact .socials i{border-color:var(--white)}

/* Footer */
.foot-brand{left:0;top:3645px;width:1200px;display:flex;justify-content:center;align-items:center;gap:10px;font-family:"Michroma",sans-serif;font-size:20px;color:var(--ink)}
.foot-brand .mark{width:10px;height:10px;background:var(--ink)}
.foot-line{left:210px;top:3718px;width:780px;border-top:1px solid var(--line);padding-top:10px;display:flex;justify-content:space-between;font-size:9px;color:var(--muted);letter-spacing:1px}
</style>
</head>
<body>

<header class="hero" role="img" aria-label="Photo of workers in hard hats on scaffolding seen from behind">
  <div class="abs brand"><span class="mark"></span>KRD Constructions</div>
  <nav class="abs nav"><a>ABOUT US</a><a>SERVICES</a><a>PROJECTS</a><a>CULTURE</a><a>NEWS</a><a>CONTACT</a></nav>
  <div class="abs hero-title display"><div class="l1">WE CONSTRUCT</div><div class="l2">ALL OVER AUSTRALIA</div></div>
  <a class="btn">Request a service</a>
  <div class="abs hero-bar">
    <span><i class="icon-dot"><svg width="10" height="10" viewBox="0 0 10 10"><path d="M2 1l2 2-1 1c1 1 2 2 3 3l1-1 2 2-1 1C5 9 1 5 1 2z" fill="#fff"/></svg></i>0400 123 765</span>
    <span><i class="icon-dot"><svg width="10" height="8" viewBox="0 0 10 8"><rect x="0.5" y="0.5" width="9" height="7" fill="none" stroke="#fff"/><path d="M.5 .5l4.5 4 4.5-4" fill="none" stroke="#fff"/></svg></i>hello@krdconstructions.com.au</span>
  </div>
  <div class="socials"><i></i><i></i><i></i><i></i></div>
</header>

<section>
  <div class="abs welcome-back"></div>
  <div class="abs welcome-photo" role="img" aria-label="Photo of a high-rise under construction with a tower crane at sunset"></div>
  <div class="abs welcome-text">
    <div class="kicker display">WELCOME TO</div>
    <div class="company">KRD Constructions</div>
    <p>Lorem ipsum dolor sit amet, consectetur adipiscing elit. Sed purus libero, itae congue at mi gravida, blandit aliquam lectus. Suspendisse auctor nisi sit amet ullamcorper sagittis. Duis lobortis mi eu tortor vestibulum, vel maximus mauris scelerisque. Duis sed justo quis sem semper tincidunt quis viverra urna. Integer sem velit, dapibus non arcu ut, cursus tincidunt diam. Aliquam aliquet mattis sed ultrices posuere. Suspendisse vitae quam nisi.</p>
    <a class="btn">Read more &nbsp;&#10230;</a>
  </div>
</section>

<section class="abs services"></section>
<h2 class="abs sec-title" style="top:1160px">Our Services</h2>
<div class="abs card service" style="left:210px;top:1235px"><div class="ph" role="img" aria-label="Line drawing of a commercial building"></div><div class="label">COMMERCIAL<br>SERVICES</div></div>
<div class="abs card service active" style="left:410px;top:1235px"><div class="ph" role="img" aria-label="Residential building exterior"></div><div class="label">RESIDENTIAL<br>SERVICES</div></div>
<div class="abs card service" style="left:612px;top:1235px"><div class="ph" role="img" aria-label="Sketch of building maintenance tools"></div><div class="label">BUILDING<br>MAINTENANCE</div></div>
<div class="abs card service" style="left:812px;top:1235px"><div class="ph" role="img" aria-label="Sketch of a building under construction"></div><div class="label">PROJECT<br>MANAGEMENT</div></div>

<h2 class="abs sec-title" style="top:1620px">Our Projects</h2>
<div class="abs filters"><span class="on">ALL</span><span>COMMERCIAL</span><span>RESIDENTIAL</span><span>CULTURAL</span></div>
<div class="abs proj" style="left:210px;top:1720px;width:177px;height:377px" role="img" aria-label="Glass office tower"></div>
<div class="abs proj" style="left:410px;top:1720px;width:177px;height:172px;background:linear-gradient(160deg,#d9cfc4,#7d6f62)" role="img" aria-label="Concrete spiral staircase"></div>
<div class="abs proj" style="left:410px;top:1925px;width:177px;height:172px;background:linear-gradient(180deg,#8fb8e3,#e8ecef)" role="img" aria-label="Curved white cultural building"></div>
<div class="abs proj" style="left:610px;top:1720px;width:177px;height:377px;background:linear-gradient(160deg,#9ccaf0,#1f5f9a)" role="img" aria-label="Mirrored glass skyscrapers"></div>
<div class="abs proj" style="left:810px;top:1720px;width:177px;height:172px;background:linear-gradient(160deg,#b8bcc0,#4e555c)" role="img" aria-label="Modern apartment facade"></div>
<div class="abs proj" style="left:810px;top:1925px;width:177px;height:172px;background:linear-gradient(160deg,#f0e6dc,#b99c80)" role="img" aria-label="Bright interior living room"></div>

<section class="abs testi"></section>
<h2 class="abs sec-title" style="top:2245px">Testimonials</h2>
<div class="abs avatar" role="img" aria-label="Photo of a client's apartment building"></div>
<div class="abs avatar-badge"></div>
<div class="abs quote-mark">&ldquo;</div>
<p class="abs quote">Lorem ipsum dolor sit amet, consectetur adipiscing elit. Sed purus libero, congue at mi gravida, blandit aliquam lectus. Suspendisse auctor nisi sit amet ullamcorper sagittis. Duis lobortis mi eu tortor vestibulum, vel maximus mauris scelerisque. Duis sed justo quis sem semper tincidunt quis viverra urna. Integer sem velit</p>
<div class="abs who"><b>MARK LOWE</b>CEO, Volta Power</div>
<div class="abs stars">&#9733;&#9733;&#9733;&#9733;&#9733;</div>

<h2 class="abs sec-title" style="top:2630px">Latest News</h2>
<article class="abs card news" style="left:210px;top:2705px"><div class="ph" role="img" aria-label="Building with infinity pool"></div><i class="badge-ic"></i><div class="date">15<small>APR</small></div><h4>LOREM IPSUM DOLOR SIT AMET, CONSECTETUR ADIPISCING ELIT</h4><p>Sed varius tellus nec felis tempor, vitae porta lacus cursus. Donec ut ante... <span>[+]</span></p></article>
<article class="abs card news" style="left:482px;top:2705px"><div class="ph" style="background:linear-gradient(180deg,#f1f3f5,#5d4a42)" role="img" aria-label="Apartment block with balconies"></div><i class="badge-ic"></i><div class="date">14<small>APR</small></div><h4>LOREM IPSUM DOLOR SIT AMET, CONSECTETUR ADIPISCING ELIT</h4><p>Sed varius tellus nec felis tempor, vitae porta lacus cursus. Donec ut ante... <span>[+]</span></p></article>
<article class="abs card news" style="left:757px;top:2705px"><div class="ph" style="background:linear-gradient(180deg,#7fb2de,#6b5a3f)" role="img" aria-label="Residential tower at dusk"></div><i class="badge-ic"></i><div class="date">12<small>APR</small></div><h4>LOREM IPSUM DOLOR SIT AMET, CONSECTETUR ADIPISCING ELIT</h4><p>Sed varius tellus nec felis tempor, vitae porta lacus cursus. Donec ut ante... <span>[+]</span></p></article>

<div class="abs map" role="img" aria-label="Street map showing the office location"></div>
<svg class="abs map-pin" width="22" height="30" viewBox="0 0 22 30"><path d="M11 0C5 0 0 5 0 11c0 8 11 19 11 19s11-11 11-19C22 5 17 0 11 0z" fill="#e53935"/><circle cx="11" cy="11" r="4" fill="#fff"/></svg>

<form class="abs form">
  <h3>GET IN TOUCH</h3>
  <div class="fields">
    <div class="field">Name:</div><div class="field">Name:</div>
    <div class="field">Phone:</div><div class="field">Service Needed:</div>
    <div class="field wide">Your Address:</div>
    <div class="field wide tall">Address:</div>
  </div>
  <a class="btn">Submit now</a>
</form>
<aside class="abs contact">
  <h3>CONTACT US</h3>
  <div class="c-row"><svg width="12" height="16" viewBox="0 0 12 16"><path d="M6 0a6 6 0 0 0-6 6c0 4 6 10 6 10s6-6 6-10a6 6 0 0 0-6-6z" fill="#fff"/></svg><div><b>KRD CONSTRUCTIONS</b><br>14 Harbour Lane<br>Northvale 2099</div></div>
  <div class="c-row"><svg width="12" height="12" viewBox="0 0 10 10"><path d="M2 1l2 2-1 1c1 1 2 2 3 3l1-1 2 2-1 1C5 9 1 5 1 2z" fill="#fff"/></svg><div><b>CALL US:</b><br>0400 123 765</div></div>
  <div class="c-row"><svg width="12" height="10" viewBox="0 0 10 8"><rect x="0.5" y="0.5" width="9" height="7" fill="none" stroke="#fff"/><path d="M.5 .5l4.5 4 4.5-4" fill="none" stroke="#fff"/></svg><div><b>MAIL US:</b><br>hello@krdconstructions.com.au</div></div>
  <div class="socials"><i></i><i></i><i></i><i></i></div>
</aside>

<footer>
  <div class="abs foot-brand"><span class="mark"></span>KRD Constructions</div>
  <div class="abs foot-line"><span>&copy; 2018 KRD CONSTRUCTIONS, ALL RIGHTS RESERVED</span><span>PRIVACY POLICY | ABOUT WEBSITE | FAQS</span></div>
</footer>

</body>
</html>
```